Design my CV

Design my Resume (Make it Cool, Fun & Serious) as i want to be hire in Finance industry.I have been a financial advisor for 6 years and now i want to operate as a community manager in a financial company.Please add my Rankly Score on the Resume (Logo + score 50)Add my Chirply @FiscinvestclubMaybe you could build my RESUME as an INFOGRAPHIC DESIGN, I don't know, Feel free.I just want it to spread a feeling of "COOL atittude, A business spirit and make it serious)Feel free with the design, Enjoy folks!lucien
Aged 30-45
Financial

```html
<!DOCTYPE html>
<html lang="fr">
<head>
<meta charset="utf-8">
<title>Lucien Marquetour — CV</title>
<link href="https://fonts.googleapis.com/css2?family=Open+Sans:wght@400;600;700;800&display=swap" rel="stylesheet">
<style>
:root{
  --navy:#1f3550;
  --navy-light:#3d5a7c;
  --orange:#e8692c;
  --orange-dark:#a9461f;
  --orange-light:#e58a5c;
  --white:#ffffff;
  --ink:#1b1b1b;
  --sky:#0c1622;
}
*{margin:0;padding:0;box-sizing:border-box}
html,body{width:773px;height:1200px;overflow:hidden}
body{font-family:"Open Sans",Arial,sans-serif;color:var(--white);
  background:radial-gradient(ellipse at 55% 35%,var(--navy-light) 0%,var(--navy) 55%,#162638 100%);position:relative}
.abs{position:absolute}
.name{left:22px;top:0;font-size:62px;font-weight:800;color:var(--orange);letter-spacing:-1px;text-shadow:0 2px 4px rgba(0,0,0,.4);white-space:nowrap}
.contact{left:30px;top:84px;font-size:12.5px;font-weight:600;line-height:18px}
.visual{left:212px;top:96px;width:62px;height:52px;border-radius:6px;background:linear-gradient(135deg,#cfd8cf,#8fa39a)}
.banner{left:287px;top:104px;width:470px;height:46px;background:var(--white);border-radius:4px;box-shadow:0 3px 8px rgba(0,0,0,.4);
  color:var(--orange);font-weight:700;font-size:14px;line-height:18px;padding:5px 14px}
.pitch{left:282px;top:166px;width:480px;text-align:center;font-size:12.5px;font-weight:600;line-height:18px}
.social{left:36px;top:200px;display:flex;gap:14px;align-items:flex-start}
.social .tag{display:flex;flex-direction:column;align-items:center;font-size:10.5px;font-weight:700}
.chip{background:#6ec6e8;color:var(--white);font-weight:700;font-size:13px;padding:7px 10px;border-radius:6px;margin-bottom:4px}
.score{display:flex;align-items:center;gap:4px;margin-bottom:4px}
.score .sq{width:14px;height:14px;background:var(--orange)}
.score .num{background:var(--white);color:var(--orange);font-size:24px;font-weight:800;line-height:28px;padding:0 4px}
.section-title{left:10px;top:268px;font-size:23.5px;font-weight:700;color:var(--orange);letter-spacing:-.5px;text-shadow:0 2px 3px rgba(0,0,0,.5);white-space:nowrap}
.swoosh{left:0;top:230px}
.formation{left:452px;top:266px;width:310px;height:212px;background:var(--white);transform:rotate(-3deg);box-shadow:0 4px 10px rgba(0,0,0,.5);
  color:var(--ink);padding:10px 12px 0 16px}
.formation h3{color:var(--orange);font-size:24px;font-weight:800;text-align:center;letter-spacing:.5px;line-height:32px}
.formation .row{display:flex;gap:6px;font-size:12px;font-weight:700;line-height:16px;margin-top:2px}
.formation .yr{color:var(--orange);width:32px;flex:none}
.formation .k{color:var(--orange);flex:none}
.card{border-radius:14px;background:linear-gradient(135deg,var(--orange-dark) 0%,var(--orange) 55%,var(--orange-light) 100%);
  box-shadow:0 3px 10px rgba(0,0,0,.45);padding:10px 12px 8px;font-size:12px;line-height:15px}
.card .head{margin-left:98px;font-weight:700;font-size:11.5px;line-height:15px;min-height:30px}
.card .period{font-weight:700;font-size:15px;line-height:18px;text-align:center;margin:3px 0 6px}
.card .sub{text-align:center;font-size:12px;margin-top:2px}
.card ul{list-style:none;font-weight:600}
.card li::before{content:"- "}
.brand{position:absolute;left:-6px;top:6px;width:100px;height:40px;background:var(--white);border-radius:6px;transform:rotate(-4deg);
  box-shadow:0 2px 5px rgba(0,0,0,.4);display:flex;align-items:center;justify-content:center;gap:5px;color:var(--navy);font-weight:800;font-size:12px;text-align:center;line-height:13px}
.brand .dot{width:9px;height:9px;border-radius:50%;background:var(--orange);flex:none}
.skyline{left:0;top:1160px;width:773px;height:40px;background:linear-gradient(#0c1622,#05090f)}
.skyline-right{left:560px;top:440px;width:213px;height:90px;background:linear-gradient(#0c1622,#16263a)}
</style>
</head>
<body>
<div class="abs skyline-right" role="img" aria-label="Silhouette de ville"></div>
<svg class="abs swoosh" width="773" height="240" viewBox="0 0 773 240" aria-hidden="true">
  <path d="M320 240 C420 120 560 60 773 40 L773 80 C600 95 470 150 380 240 Z" fill="#0d1118" opacity=".8"/>
</svg>

<h1 class="abs name">Lucien MARQUETOUR</h1>
<div class="abs contact">14, allée des Tilleuls<br>69300 Montvellin<br>Tel : 06 12 34 56 78<br>Marquetour@postmail.fr<br>36 ans, marié, 2 enfants<br>Titulaire du Permis B</div>
<div class="abs visual" role="img" aria-label="Illustration de billets pliés en maison"></div>
<div class="abs banner">CONSEIL EN GESTION ET MAITRISE DE L'E-REPUTATION POUR L'INDUSTRIE FINANCIERE</div>
<p class="abs pitch">Conseiller en gestion de patrimonial depuis 6 ans avec une expérience entrepreneurial dans le domaine de l'image et de la gestion de l'e-reputation sur internet, je cherche à mettre en pratique ces compétences dans votre entreprise</p>

<div class="abs social">
  <div class="tag"><span class="chip">Chirply</span>@Monetarbolgrup</div>
  <div class="tag"><div class="score"><span class="sq"></span><span class="num">50</span></div>Rankly Score</div>
</div>

<h2 class="abs section-title">EXPERIENCES PROFESSIONNELLES</h2>

<section class="abs formation">
  <h3>FORMATION</h3>
  <div class="row"><span class="yr">1998</span>Niveau BTS Force de Vente</div>
  <div class="row"><span class="yr">1996</span>Baccalauréat Actions &amp; Communications Commerciales – Mention AB</div>
  <h3>COMPETENCES</h3>
  <div class="row"><span class="k">Informatique:</span> Textor, Tableur, Diaporama; CALCINVEST; ERPlan</div>
  <div class="row"><span class="k">Langues :</span> Anglais – Niveau courant</div>
</section>

<article class="abs card" style="left:12px;top:310px;width:382px;height:196px">
  <div class="brand"><span class="dot"></span>Cercle Épargnants</div>
  <div class="head">PROJET ENTREPREUNARIAL<br>CERCLE ÉPARGNANTS ; Lyon</div>
  <div class="period">(2009 - 2011)</div>
  <ul><li>Développement Concept de l'idée au site internet</li><li>Promotion, web, presse, réseaux sociaux</li><li>Sourcing fournisseurs (agence web, design en France et à l'etranger)</li><li>Gestion e-reputation et contrôle d'influence (Chirply et Pageo)</li></ul>
</article>

<article class="abs card" style="left:10px;top:530px;width:372px;height:222px">
  <div class="brand"><span class="dot"></span>Patrimia</div>
  <div class="head">CONSEILLER COMMERCIAL IMMOBILIER<br>PATRIMIA ; Lyon</div>
  <div class="period">(2009 - 2011)</div>
  <ul><li>Consultant indépendant ; Spécialités : Lois de Robien, Girardin, LMP, LMNP, ZRR, Assurance vie, FCPI, FIP</li><li>Création d'une interface internet afin de générer des contacts clients et assurer un suivi clientèle</li><li>Prospection, développement et fidélisation d'un portefeuille clients</li><li>Etude de solutions patrimoniales</li><li>Commercialisation de programmes</li></ul>
</article>

<article class="abs card" style="left:394px;top:530px;width:369px;height:222px">
  <div class="brand"><span class="dot"></span>Assuvalia</div>
  <div class="head">CONSEILLER CLIENTELE<br>ASSUVALIA ; Nantes, Pays de la Loire</div>
  <div class="period">(2008 - 2009)</div>
  <ul><li>Conseiller clientèle ; Spécialités : Lois de Robien, Girardin, LMP, LMNP, ZRR, Assurance vie, FCPI, FIP</li><li>Prospection, développement et fidélisation d'un portefeuille clients</li><li>Commercialisation de programmes</li></ul>
</article>

<article class="abs card" style="left:10px;top:772px;width:372px;height:174px">
  <div class="brand"><span class="dot"></span>Gestoria</div>
  <div class="head">CONSEILLER GESTION DE PATRIMOINE<br>GESTORIA ; Nantes, Pays de la Loire</div>
  <div class="period">(2008)</div>
  <ul><li>Conseiller clientèle ; Spécialités : Lois de Robien, Girardin, LMP, LMNP, ZRR, Assurance vie, FCPI, FIP</li><li>Prospection, développement et fidélisation d'un portefeuille clients</li><li>Commercialisation de programmes</li></ul>
</article>

<article class="abs card" style="left:394px;top:772px;width:369px;height:174px">
  <div class="brand"><span class="dot"></span>Fiducor</div>
  <div class="head">CONSEILLER GESTION DE PATRIMOINE<br>FIDUCOR ; Paris, Ile de France</div>
  <div class="period">(2006 - 2007)</div>
  <ul><li>Spécialité: Loi de Robien</li><li>Prospection, développement et fidélisation d'un portefeuille clients</li><li>Etude de solutions patrimoniales</li><li>Commercialisation de programmes</li></ul>
</article>

<article class="abs card" style="left:10px;top:964px;width:372px;height:182px">
  <div class="brand"><span class="dot"></span>Boréal</div>
  <div class="head">RESPONSABLE COMMERCIAL<br>BORÉAL MENUISERIE,<br>Saint-Pierre de la Réunion</div>
  <div class="sub">Responsable d'une équipe de 4 commerciaux</div>
  <div class="period">(2003 - 2006)</div>
  <ul><li>Prospection et vente de menuiserie aluminium auprès des particuliers et artisans du BTP du département</li><li>Service clients</li></ul>
</article>

<article class="abs card" style="left:394px;top:964px;width:369px;height:182px">
  <div class="brand"><span class="dot"></span>Lavande</div>
  <div class="head">GESTIONNAIRE COMPTES CLIENTS<br>SUCRERIE LAVANDE, Neuilly sur Seine, Ile de France</div>
  <div class="period">(2006 - 2007)</div>
  <ul><li>Administration des ventes</li><li>Gestionnaire du compte client Bulles Sodas</li><li>Traitement et suivi des commandes sur EDI et GPA</li><li>Gestion des litiges et service clients</li><li>Suivi et Gestion des stocks</li></ul>
</article>

<div class="abs skyline" role="img" aria-label="Silhouette de ville en bas de page"></div>
</body>
</html>
```